依頼詳細
商品名は「WHEY PROTEIN ISOLATE」です。一般的なプロテインよりも脂肪・糖質を極力排除しており、高純度のたんぱく質を摂取でき、効率的に引き締まった体を作れるのが特徴になります。

メインユーザーは30~40代。男女比はほぼ1:1です。

現行のものは栄養士またはトレーナーがカウンセリングしてから提供することを想定して、名前・量・飲み方を記載して提供できるようにしています(添付ファイルをご覧下さいませ)。レイアウトやデザインは変えてもいいですが、これらの項目自体は変えないようにお願いいたします。

現行品のシンプルさ・清潔感を保ちつつも、「プレミアム」な印象を持てるものになると嬉しいです。

<例1(フォルテン)>
http://shop.forten.jp/products/list.php?category_id=7
<例2(ネクサリオン)>
https://www.nexarion.jp/sports-nutrition/solid-core-blend/48271605.html

以上、よいご提案をお待ちしております。
ご不明な点がございましたら、お気軽にお問い合せ下さいませ。
記載項目
スタンドアルミパウチ:横218mm×縦340mm(チャック下310mm)
※現行品はシールに印刷して貼っていますが、リニューアル品はパウチに印刷しますので、印刷範囲の指定はございません。
希望イメージ
シンプル 複雑
単色 カラフル
暗い 明るい
日常 高級
遊び心 厳粛
未来的 伝統的
女性的 男性的
希望する色
カラーは白地にエメラルドグリーン(DIC63)でお願いいたします。他の色を追加してもOKです。
納品ファイル
• イラストレーター形式 (.ai)
補足説明
選定後はアウトライン化されているファイルと、されていないファイルの両方をお送り下さい。
パーソナルジムに陳列するプロテインですので…あまりにエステっぽいといいますか、女性的なデザインは好ましくないかと思います。
重ねて申し上げますが、シンプルにお願いいたします。<例>もよくご覧下さいませ。
■ 選んだ理由

他にもいいご提案があり悩みましたが、インストラクション部分のデザインが見やすい点が決め手になりました。

■ 提案者全員のお礼・コメント

たくさんのご提案ありがとうございました。また機会がありましたらぜひよろしくお願い致します。

```html
<!DOCTYPE html>
<html lang="en">
<head>
<meta charset="UTF-8">
<title>Whey Protein Isolate – Pouch Label</title>
<link rel="stylesheet" href="https://fonts.googleapis.com/css2?family=Oswald:wght@500;700&family=Roboto:wght@400;500&display=swap">
<style>
  :root {
    --emerald: #4fa37f;
    --emerald-deep: #3d8c69;
    --emerald-pale: #cfe8dc;
    --emerald-mist: #eaf5ef;
    --ink: #5a5a5a;
    --paper: #ffffff;
  }
  * { margin: 0; padding: 0; box-sizing: border-box; }
  html, body {
    width: 815px; height: 1200px; overflow: hidden;
    background: var(--paper);
  }
  .pouch-face {
    position: relative;
    width: 815px; height: 1200px;
    background: var(--paper);
    font-family: "Roboto", Arial, sans-serif;
    color: var(--ink);
  }
  .ornament-frame {
    position: absolute;
    left: 55px; right: 55px; top: 150px; height: 500px;
    border-radius: 40px;
    background: radial-gradient(ellipse at center, var(--paper) 38%, var(--emerald-mist) 62%, var(--emerald-pale) 100%);
  }
  .title-block {
    position: absolute; left: 0; right: 0; top: 285px;
    text-align: center;
  }
  .product-name {
    font-family: "Oswald", Impact, sans-serif;
    font-weight: 700;
    font-size: 112px;
    line-height: 1;
    color: var(--emerald);
    letter-spacing: 1px;
  }
  .product-type {
    font-family: "Oswald", Impact, sans-serif;
    font-weight: 700;
    font-size: 44px;
    line-height: 1;
    margin-top: 6px;
    color: var(--emerald);
    letter-spacing: 3px;
  }
  .tagline {
    margin-top: 22px;
    font-size: 13px;
    line-height: 1.55;
    font-weight: 500;
    color: var(--emerald-deep);
  }
  .prescription {
    position: absolute; left: 110px; width: 595px; top: 665px;
    display: grid; grid-template-columns: 1fr 1fr; column-gap: 28px;
    font-size: 12px;
  }
  .field-label {
    display: block;
    padding-bottom: 22px;
    border-bottom: 1.5px solid var(--emerald);
    color: var(--ink);
  }
  .section-head {
    display: block;
    margin-top: 16px;
    padding-bottom: 5px;
    border-bottom: 1.5px solid var(--emerald);
    font-size: 11.5px;
  }
  .choice-row { display: flex; gap: 34px; margin-top: 14px; }
  .choice-list { list-style: none; margin-top: 10px; }
  .choice-list li, .choice-row span {
    display: flex; align-items: center; gap: 14px;
    height: 24px; letter-spacing: 0.5px;
  }
  .tick-box {
    width: 12px; height: 12px;
    border: 1.2px solid var(--ink);
    flex: none;
  }
  .blank-paren { word-spacing: 90px; }
  .brand-mark {
    position: absolute; left: 0; right: 0; top: 1010px;
    display: flex; justify-content: center; align-items: center; gap: 12px;
    font-family: "Oswald", Impact, sans-serif;
    font-weight: 500;
    font-size: 26px;
    letter-spacing: 4px;
    color: var(--emerald);
  }
  .brand-square {
    width: 22px; height: 22px;
    background: var(--emerald);
  }
</style>
</head>
<body>
  <main class="pouch-face">
    <div class="ornament-frame" role="img" aria-label="Decorative green filigree scrollwork framing the product name"></div>

    <header class="title-block">
      <h1 class="product-name">WHEYPROTEIN</h1>
      <p class="product-type">ISOLATE</p>
      <p class="tagline">The finest way to build lean muscle from pure whey protein.<br>Mix one serving with cold water or milk and drink it soon after your training session.</p>
    </header>

    <section class="prescription">
      <div class="column">
        <span class="field-label">Name</span>
        <div class="choice-row">
          <span><i class="tick-box"></i>WATER</span>
          <span><i class="tick-box"></i>MILK</span>
        </div>
        <span class="section-head">Recommended intake per once</span>
        <ul class="choice-list">
          <li><i class="tick-box"></i>2 SPOON / 100cc</li>
          <li><i class="tick-box"></i>3 SPOON / 200cc</li>
          <li><i class="tick-box"></i>4 SPOON / 400cc</li>
          <li><i class="tick-box"></i><span class="blank-paren">( )</span></li>
        </ul>
      </div>
      <div class="column">
        <span class="field-label">Drink</span>
        <span class="section-head" style="margin-top:52px">Recommended timing</span>
        <ul class="choice-list">
          <li><i class="tick-box"></i>BREAKFAST</li>
          <li><i class="tick-box"></i>AFTER EXERCIZE</li>
          <li><i class="tick-box"></i>BEFORE SLEEP</li>
          <li><i class="tick-box"></i><span class="blank-paren">( )</span></li>
        </ul>
      </div>
    </section>

    <footer class="brand-mark">
      <span class="brand-square"></span>
      <span class="brand-name">KORVANTA</span>
    </footer>
  </main>
</body>
</html>
```